App Design Project

Hello,
I'm looking for a great designer for my iOS Applications, we have a lot of works and we're short in designers :(
I want to revamp my thermometer iOS app. You will find attached the images I want to replace. I need something with the same element (temp, condition, weather icon) but with a different look!
Same, new icon, you have carte blanche to this one.
I want a design that stands out from the hundreds of weather application that almost all the same design. I am looking for something that does say "wow, it rocks."
Please do not Provide classic design that we can see everywhere ... I'm looking for something with a real artistic choice, contrast, colours, etc.
As a marketing screenshot, I want something classic, you'll find an example attached, feel free to innovate.
To sum-up :
- One new view for my App
- One new icon
- One marketing screenshot
Marketing

```html
<!DOCTYPE html>
<html lang="en">
<head>
<meta charset="utf-8">
<title>Thermometer App – Weather Views</title>
<link rel="stylesheet" href="https://fonts.googleapis.com/css2?family=Inter:wght@100;400&family=League+Spartan:wght@700&family=Noto+Serif:ital,wght@1,700&display=swap">
<style>
  :root {
    --ink: #1e1e1e;
    --paper: #efefef;
    --paper-light: #fafafa;
    --paper-shade: #e2e2e2;
    --sky-top: #2e8bdb;
    --sky-mid: #62aee6;
    --sky-low: #5ec6ec;
    --sky-bottom: #3cc3e6;
    --sun-top: #f3674f;
    --sun-mid: #f7885a;
    --sun-low: #f8a062;
    --sun-bottom: #f8aa6a;
    --sun-disc: #f07c4a;
    --white: #ffffff;
  }
  html, body {
    margin: 0;
    padding: 0;
    overflow: hidden;
  }
  body {
    width: 1200px;
    height: 900px;
    background: var(--paper);
  }
  .showcase {
    display: flex;
    width: 1200px;
    height: 900px;
    overflow: hidden;
  }
  .weather-view {
    display: block;
    width: 600px;
    height: 900px;
  }
  .condition {
    font-family: "Inter", "Helvetica Neue", sans-serif;
    font-weight: 100;
    text-anchor: middle;
  }
  .condition--light { fill: var(--white); }
  .condition--dark { fill: var(--ink); }
  .details {
    font-family: "Inter", "Helvetica Neue", sans-serif;
    font-weight: 400;
    font-size: 19px;
    fill: var(--ink);
    text-anchor: middle;
  }
  .temp-main, .temp-unit, .temp-alt {
    font-family: "League Spartan", "Futura", sans-serif;
    font-weight: 700;
    fill: var(--ink);
  }
  .temp-main { font-size: 190px; letter-spacing: -2px; }
  .temp-unit { font-size: 100px; }
  .temp-alt { font-size: 72px; }
  .degree { fill: none; stroke: var(--ink); stroke-width: 4; }
  .divider { stroke: var(--ink); stroke-width: 1; }
  .refresh { fill: none; stroke: var(--ink); stroke-width: 4; }
  .refresh-head { fill: var(--ink); }
  .info {
    font-family: "Noto Serif", Georgia, serif;
    font-style: italic;
    font-weight: 700;
    font-size: 50px;
    fill: var(--ink);
  }
  .fold-light { fill: var(--paper-light); }
  .fold-shade { fill: var(--paper-shade); }
  .fold-veil { fill: var(--white); opacity: 0.32; }
  .sun-disc { fill: var(--sun-disc); opacity: 0.55; }
</style>
</head>
<body>
<main class="showcase">

  <!-- Partly cloudy view -->
  <svg class="weather-view" viewBox="0 0 500 750" aria-label="Partly cloudy, 28 degrees Celsius">
    <defs>
      <linearGradient id="cloudy-top" x1="0" y1="0" x2="0.3" y2="1">
        <stop offset="0" stop-color="var(--sky-top)"/>
        <stop offset="0.7" stop-color="var(--sky-mid)"/>
        <stop offset="1" stop-color="#9fd0ef"/>
      </linearGradient>
      <linearGradient id="cloudy-bottom" x1="0" y1="0" x2="1" y2="0.6">
        <stop offset="0" stop-color="#b9dff2"/>
        <stop offset="0.45" stop-color="var(--sky-low)"/>
        <stop offset="1" stop-color="var(--sky-bottom)"/>
      </linearGradient>
    </defs>
    <rect class="fold-light" x="0" y="0" width="500" height="750"/>
    <polygon class="fold-shade" points="350,300 500,130 500,480 420,380"/>
    <polygon class="fold-light" points="350,0 500,0 500,130 350,300"/>
    <polygon class="fold-shade" points="0,315 70,315 0,372"/>
    <polygon class="fold-shade" points="310,475 500,300 500,475"/>
    <rect role="img" aria-label="Blue sky with soft drifting clouds" x="0" y="0" width="350" height="315" fill="url(#cloudy-top)"/>
    <rect role="img" aria-label="Bright blue sky with soft clouds" x="0" y="475" width="500" height="275" fill="url(#cloudy-bottom)"/>
    <polygon class="fold-veil" points="0,475 405,475 150,695 0,560"/>

    <text class="condition condition--light" x="165" y="128" font-size="68">PARTLY</text>
    <text class="condition condition--light" x="165" y="205" font-size="68">CLOUDY</text>
    <text class="details" x="175" y="262">HUMIDITY: 87%</text>
    <text class="details" x="175" y="294">N/NW AT 8 MPH</text>

    <text class="temp-main" x="56" y="470">28</text>
    <circle class="degree" cx="306" cy="333" r="12"/>
    <text class="temp-unit" x="318" y="420">C</text>

    <line class="divider" x1="0" y1="513" x2="420" y2="513"/>
    <path class="refresh" d="M446 502 A12 12 0 1 1 442 523"/>
    <polygon class="refresh-head" points="433,523 444,515 445,530"/>

    <text class="temp-alt" x="62" y="608">82.4</text>
    <circle class="degree" cx="283" cy="552" r="11"/>
    <text class="temp-alt" x="312" y="608">F</text>

    <text class="info" x="432" y="702">i</text>
  </svg>

  <!-- Sunny view -->
  <svg class="weather-view" viewBox="0 0 500 750" aria-label="Sunny, 32 degrees Celsius">
    <defs>
      <linearGradient id="sunny-top" x1="0" y1="0" x2="0" y2="1">
        <stop offset="0" stop-color="var(--sun-top)"/>
        <stop offset="1" stop-color="var(--sun-mid)"/>
      </linearGradient>
      <linearGradient id="sunny-bottom" x1="0" y1="0" x2="1" y2="1">
        <stop offset="0" stop-color="var(--sun-mid)"/>
        <stop offset="0.5" stop-color="var(--sun-low)"/>
        <stop offset="1" stop-color="var(--sun-bottom)"/>
      </linearGradient>
    </defs>
    <rect class="fold-light" x="0" y="0" width="500" height="750"/>
    <polygon class="fold-shade" points="350,300 500,130 500,480 420,380"/>
    <polygon class="fold-light" points="350,0 500,0 500,130 350,300"/>
    <polygon class="fold-shade" points="0,315 70,315 0,372"/>
    <polygon class="fold-shade" points="310,475 500,300 500,475"/>
    <rect x="0" y="0" width="350" height="315" fill="url(#sunny-top)"/>
    <rect x="0" y="475" width="500" height="275" fill="url(#sunny-bottom)"/>
    <polygon class="fold-veil" points="0,475 405,475 150,695 0,560"/>
    <circle class="sun-disc" cx="230" cy="657" r="77"/>

    <text class="condition condition--dark" x="170" y="175" font-size="80">SUNNY</text>
    <text class="details" x="175" y="262">HUMIDITY: 87%</text>
    <text class="details" x="175" y="294">N/NW AT 8 MPH</text>

    <text class="temp-main" x="56" y="470">32</text>
    <circle class="degree" cx="306" cy="333" r="12"/>
    <text class="temp-unit" x="318" y="420">C</text>

    <line class="divider" x1="0" y1="513" x2="420" y2="513"/>
    <path class="refresh" d="M446 502 A12 12 0 1 1 442 523"/>
    <polygon class="refresh-head" points="433,523 444,515 445,530"/>

    <text class="temp-alt" x="62" y="608">89.6</text>
    <circle class="degree" cx="283" cy="552" r="11"/>
    <text class="temp-alt" x="312" y="608">F</text>

    <text class="info" x="432" y="702">i</text>
  </svg>

</main>
</body>
</html>
```